International Honeymoon Tour Operator needs Business Card

We need to design a business card including our new logo for a new tour operator called Marisol Thorne Getaways. We would like to also include the text 'Personal Tailor-Made Honeymoons for our Guests at a Lower Cost'. Please Include the following details as well; 'Website: www.marisolthornegetaways.co.uk'; 'E-mail: felix@marisolthornegetaways.co.uk'; 'Mobile: 07914263058'. We would like the design to be compatible with the logo and text. The final design should communicate professionalism, modern and ethical.

We want to business card to be double sided.

We would like to be able to easily adjust the e-mail address and contact number in the future for other employees either through you or ourselves.

Target Market(s)

Brides and grooms aged 18-35 predominantly.

Industry/Entity Type

Business

Colors

Designer to choose colors to be used in the design.

Requirements
Must have
• Logo
Requested Text
Double sided
Nice to have
• Additional colour
The wow factor
Should not have
• Images of currency

```html
<!DOCTYPE html>
<html lang="en">
<head>
<meta charset="utf-8">
<title>Marisol Thorne Getaways – Business Card</title>
<link rel="stylesheet" href="https://fonts.googleapis.com/css2?family=Questrial&family=Arimo:wght@400&display=swap">
<style>
  :root {
    --page-bg: #e6e7e6;
    --card-white: #ffffff;
    --brand-lime: #a6d64b;
    --brand-teal: #3b6b60;
    --brand-dark: #2c5048;
    --text-white: #ffffff;
  }
  html, body {
    margin: 0;
    padding: 0;
    width: 1200px;
    height: 1076px;
    overflow: hidden;
    background: var(--page-bg);
  }
  .canvas {
    position: relative;
    width: 1200px;
    height: 1076px;
  }
  .card {
    position: absolute;
    left: 320px;
    width: 560px;
    height: 320px;
    box-shadow: 0 6px 18px rgba(0,0,0,0.18);
    overflow: hidden;
  }
  .card--front {
    top: 150px;
    background: var(--card-white);
  }
  .card--back {
    top: 606px;
    background: var(--brand-lime);
  }
  .brand {
    position: absolute;
    left: 0;
    right: 0;
    top: 92px;
    display: flex;
    flex-direction: column;
    align-items: center;
    gap: 18px;
  }
  .brand__mark {
    width: 54px;
    height: 54px;
    border-radius: 50%;
    background: var(--brand-teal);
  }
  .brand__name {
    font-family: "Questrial", sans-serif;
    font-weight: 400;
    font-size: 30px;
    letter-spacing: 2px;
    color: var(--brand-teal);
    margin: 0;
  }
  .tagline-band {
    position: absolute;
    left: 0;
    right: 0;
    bottom: 0;
    height: 52px;
    background: var(--brand-lime);
    display: flex;
    align-items: center;
    justify-content: center;
  }
  .tagline {
    font-family: "Arimo", sans-serif;
    font-size: 17px;
    color: var(--text-white);
    margin: 0;
    white-space: nowrap;
  }
  .contact {
    position: absolute;
    left: 70px;
    top: 110px;
    display: grid;
    grid-template-columns: 70px auto;
    column-gap: 14px;
    row-gap: 10px;
    font-family: "Arimo", sans-serif;
    font-size: 17px;
    margin: 0;
  }
  .contact dt {
    color: var(--text-white);
    text-align: right;
    font-size: 14px;
    line-height: 20px;
  }
  .contact dd {
    margin: 0;
    color: var(--brand-dark);
    line-height: 20px;
    white-space: nowrap;
  }
</style>
</head>
<body>
<main class="canvas">
  <section class="card card--front" aria-label="Card front">
    <div class="brand">
      <span class="brand__mark"></span>
      <h1 class="brand__name">Marisol Thorne Getaways</h1>
    </div>
    <div class="tagline-band">
      <p class="tagline">Personal Tailor-Made Honeymoons for our Guests at a Lower Cost</p>
    </div>
  </section>

  <section class="card card--back" aria-label="Card back">
    <dl class="contact">
      <dt>web:</dt>
      <dd>www.marisolthornegetaways.co.uk</dd>
      <dt>email:</dt>
      <dd>felix@marisolthornegetaways.co.uk</dd>
      <dt>mobile:</dt>
      <dd>07914263058</dd>
    </dl>
  </section>
</main>
</body>
</html>
```